Webdesign for large cottage directory

We have developed a first version of a website that can accommodate large groups (10 to 300 people). The site is English and is aimed at a wide audience ranging from a group of students to a family or a family. For the visitors the site is free and it is the propietaires who pay to see their accommodation. The site is online with just a few fake lodgings and a simple design to the elements that must be appraised (nothing to keep the current design). Our website is here: 456abri.com (login / pass = admin / 123) Home page (456abri.com): on this page section) and lodging by theme (third section). These three points should be highlighted as possible. The displayed map may be slightly modified. Only the background and the color changes when hovering over the mouse. It can be enlarged / retreciated. Below these 3 sections we have some fairly published articles, the latest blog posts and the footer. The menu will be visible throughout the site. Category page (https://456abri.fr/gite-departement/aveyron OR https://456abri.fr/gites-couchages-121): On these pages we always return the same format with the googlemap, an image 1 text. Below the list of the cottages concerned and the filter options. Product page: The pages presenting the cottages can be of two types: - Either the cottage has no owner and there is no contact for the visitor to the owner that he can retrieve his cottage by registering: example of a page of this type: https://456abri.fr/domaine-de-varnoquet - The cottage to a propietaire and we are on the classic card. : // 456abri. en / domain-of-varnoquet2 For all products on the site we have nav tab. It's just for testing. We do not want to be in the design for real website. All information must be in the page without login / register page: classic, it's here: https://456abri.it/login and https://456abri.fr/register Blog homepage (https://456abri.fr/blog ): Classic blog page Blog post (https://456abri.fr/blog/urltemporaire1551521154) and static page (https://456abri.fr/blog/Systeme-classement-456abrifr): Nothing special Menu: Menu is an important part of the website. It's the way to navigate on the wbesite.
Number of Pages Required
4 page
Colors
Designer to choose colors to be used in the design.
Look and feel

```html
<!DOCTYPE html>
<html lang="fr">
<head>
<meta charset="utf-8">
<title>456abri.Fr – Connexion</title>
<link href="https://fonts.googleapis.com/css2?family=Roboto:wght@400;500;700&family=Montserrat:wght@400;500;600;700&family=Roboto+Condensed:wght@400;500;700&display=swap" rel="stylesheet">
<style>
:root{
  --navy:#0e3a6b;
  --navy-dark:#0b2f58;
  --panel:rgba(24,68,118,0.93);
  --orange:#f7930a;
  --card:#f0f1fb;
  --white:#ffffff;
  --text:#1b1b1b;
  --link:#2b8fd6;
  --map:#9db2cc;
}
*{box-sizing:border-box;margin:0;padding:0}
html,body{width:994px;height:1200px;overflow:hidden;background:var(--white)}
body{position:relative;font-family:"Roboto",sans-serif;color:var(--text)}
.abs{position:absolute}

/* header */
.topbar{left:0;top:0;width:994px;height:34px}
.topbar-item{top:9px;color:var(--white);font:500 12.5px "Roboto",sans-serif;display:flex;align-items:center;gap:6px}
.round-icon{width:18px;height:18px;border:1.5px solid var(--white);border-radius:50%;display:inline-block}
.socials{top:8px;left:917px;display:flex;gap:3px}
.brand{left:20px;top:40px;display:flex;align-items:center;gap:12px}
.brand-mark{width:42px;height:42px;border:3px solid var(--orange)}
.brand-name{font:700 31px "Roboto",sans-serif;color:var(--navy)}
.account{top:58px;display:flex;align-items:center;gap:6px;font:500 12.5px "Roboto",sans-serif;color:var(--text)}
.sep{top:56px;width:1px;height:20px;background:#ccc}

/* navigation */
.mainnav{left:0;top:96px;width:994px;height:38px;background:var(--navy)}
.nav-item{top:11px;color:var(--white);font:500 13.5px "Roboto",sans-serif;display:flex;align-items:center;gap:6px}
.nav-item.active{color:var(--orange)}
.caret{width:0;height:0;border-left:5px solid transparent;border-right:5px solid transparent;border-top:5px solid currentColor}

/* login */
.login-card{left:76px;top:210px;width:842px;height:532px;background:var(--card);border-radius:6px}
.field{left:191px;width:612px;height:54px;background:var(--white);border:2px solid #e6e7f0;border-radius:6px;font:500 17px "Montserrat",sans-serif;padding:0 20px;display:flex;align-items:center;justify-content:space-between}
.remember{left:190px;top:455px;display:flex;align-items:center;gap:10px;font:400 14.5px "Montserrat",sans-serif}
.radio{width:24px;height:24px;border:1.5px solid #333;border-radius:50%;background:var(--white)}
.submit{left:388px;top:501px;width:219px;height:50px;background:var(--navy);border-radius:6px;color:var(--white);font:700 17px "Montserrat",sans-serif;display:flex;align-items:center;justify-content:center}
.forgot{left:0;width:994px;top:600px;text-align:center;font:400 14.5px "Montserrat",sans-serif;color:var(--link)}
.forgot span{border-bottom:1px solid var(--link);padding-bottom:1px}
.social-login{left:0;width:994px;top:676px;display:flex;justify-content:center;align-items:center;gap:10px;font:500 14.5px "Montserrat",sans-serif}
.social-dot{width:26px;height:26px;border-radius:50%;border:4px solid var(--orange)}

/* dropdown */
.dept-menu{left:283px;top:134px;width:402px;height:432px;background:var(--panel)}
.dept-map{left:24px;top:20px;width:354px;height:392px;border-radius:40% 30% 35% 30%;background:radial-gradient(ellipse at 50% 45%,var(--map) 60%,rgba(157,178,204,0.6) 75%,transparent 78%)}

/* footer */
.footer{left:0;top:819px;width:994px;height:348px;background:linear-gradient(180deg,#1e5088 0%,#163f70 55%,#0d2e57 100%);color:var(--white);font-family:"Roboto Condensed",sans-serif}
.footer-brand{left:0;width:994px;top:80px;display:flex;justify-content:center;align-items:center;gap:14px}
.footer-brand .brand-mark{width:46px;height:46px}
.footer-brand .brand-name{color:var(--white);font-size:31px}
.col-title{top:145px;font:700 12.5px "Roboto",sans-serif;letter-spacing:.3px;padding-bottom:8px;border-bottom:1px solid rgba(255,255,255,.5)}
.col-list{top:185px;font:500 11.5px "Roboto Condensed",sans-serif;line-height:16px}
.line-icon{display:flex;align-items:flex-start;gap:7px}
.line-icon .round-icon{width:16px;height:16px;flex:none}
.social-row{display:flex;align-items:center;gap:10px;height:30px}
.social-row .sq{width:20px;height:20px;border-radius:4px;background:rgba(255,255,255,.35)}
.news-input{left:649px;top:229px;width:215px;height:27px;border-radius:14px;background:var(--white);color:#333;font:500 12px "Roboto",sans-serif;padding:6px 16px}
.news-btn{left:649px;top:264px;width:108px;height:25px;border-radius:13px;background:var(--orange);font:700 11px "Roboto",sans-serif;display:flex;align-items:center;justify-content:center}
.copyright{left:0;top:1167px;width:994px;height:33px;background:var(--orange);color:var(--white);font:700 9.5px "Roboto",sans-serif;display:flex;align-items:center;justify-content:center;letter-spacing:.3px}
</style>
</head>
<body>

<header>
  <svg class="abs topbar" width="994" height="34" viewBox="0 0 994 34"><polygon points="593,0 994,0 994,34 608,34" fill="var(--navy-dark)"/></svg>
  <div class="abs topbar-item" style="left:625px"><span class="round-icon"></span>1800.555.0192</div>
  <div class="abs topbar-item" style="left:768px"><span class="round-icon"></span>info@456abri.fr</div>
  <div class="abs socials"><span class="round-icon"></span><span class="round-icon"></span><span class="round-icon"></span></div>

  <div class="abs brand"><span class="brand-mark"></span><span class="brand-name">456abri.Fr</span></div>

  <div class="abs account" style="left:762px">
    <svg width="14" height="16" viewBox="0 0 14 16"><circle cx="6" cy="4" r="3" fill="var(--navy)"/><path d="M2 15 L3 9 H11 L12 15Z" fill="var(--navy)"/></svg>Register</div>
  <div class="abs sep" style="left:842px"></div>
  <div class="abs account" style="left:855px">
    <svg width="14" height="16" viewBox="0 0 14 16"><path d="M3 7 V4 a4 4 0 0 1 8 0 V7" stroke="var(--navy)" stroke-width="2" fill="none"/><rect x="1" y="7" width="12" height="9" rx="1" fill="var(--navy)"/></svg>Login</div>
  <div class="abs sep" style="left:919px"></div>
  <div class="abs account" style="left:932px"><span style="width:14px;height:14px;border-radius:50%;background:#2a4b8d;display:inline-block"></span>EN
    <svg width="10" height="8" viewBox="0 0 10 8"><path d="M1 2 L5 6 L9 2" stroke="#222" stroke-width="1.6" fill="none"/></svg></div>
</header>

<nav class="abs mainnav">
  <div class="abs nav-item" style="left:63px">Home</div>
  <div class="abs nav-item" style="left:141px">Gîte par capacité <span class="caret"></span></div>
  <div class="abs nav-item active" style="left:297px">Gîte par département <span class="caret"></span></div>
  <div class="abs nav-item" style="left:479px">Gîte par thématique <span class="caret"></span></div>
  <div class="abs nav-item" style="left:652px">Blog</div>
  <div class="abs nav-item" style="left:721px">Vos Favoris</div>
  <div class="abs nav-item" style="left:835px">Contactez nous</div>
</nav>

<main>
  <div class="abs login-card"></div>
  <div class="abs field" style="top:325px">Adresse email
    <svg width="20" height="16" viewBox="0 0 20 16"><rect x="1" y="1" width="18" height="14" fill="none" stroke="var(--orange)" stroke-width="1.6"/><path d="M1 1 L10 9 L19 1 M1 15 L8 8 M19 15 L12 8" fill="none" stroke="var(--orange)" stroke-width="1.6"/></svg></div>
  <div class="abs field" style="top:390px">Mot de passe
    <svg width="18" height="24" viewBox="0 0 18 24"><path d="M4 10 V6 a5 5 0 0 1 10 0 V10" stroke="var(--orange)" stroke-width="2.4" fill="none"/><rect x="1" y="10" width="16" height="13" rx="3" fill="var(--orange)"/><rect x="8" y="14" width="2" height="5" fill="#fff"/></svg></div>
  <div class="abs remember"><span class="radio"></span>Se souvenir de moi</div>
  <div class="abs submit">Entrer</div>
  <div class="abs forgot"><span>Avez-vous oublié votre mot de passe ?</span></div>
  <div class="abs social-login"><span class="social-dot"></span>Se connecter ave Nuvio</div>

  <div class="abs dept-menu">
    <div class="abs dept-map" role="img" aria-label="Carte de France des départements"></div>
  </div>
</main>

<footer class="abs footer" role="img" aria-label="Pied de page sur fond de vue de Paris">
  <div class="abs footer-brand"><span class="brand-mark"></span><span class="brand-name">456abri.Fr</span></div>

  <div class="abs col-title" style="left:132px;width:108px">QUICK LINKS</div>
  <div class="abs col-list" style="left:132px">Gîte par capacité<br>Gîte par département<br>Gîte par thématique<br>Blog<br>Contactez nous</div>

  <div class="abs col-title" style="left:311px;width:117px">CONTACT</div>
  <div class="abs col-list" style="left:308px">
    <div class="line-icon"><span class="round-icon"></span><span>456Abri.fr<br>123 Lorem Ipsum Dr<br>Paris, France</span></div>
    <div class="line-icon" style="margin-top:14px"><span class="round-icon"></span><span>1800.555.0192</span></div>
    <div class="line-icon" style="margin-top:15px"><span class="round-icon"></span><span>info@456abri.fr</span></div>
  </div>

  <div class="abs col-title" style="left:498px;width:82px">FOLLOW US</div>
  <div class="abs col-list" style="left:497px;top:176px">
    <div class="social-row"><span class="sq"></span>friendbook</div>
    <div class="social-row"><span class="sq"></span>chirpnet</div>
    <div class="social-row"><span class="sq"></span>pictogram</div>
  </div>

  <div class="abs col-title" style="left:651px;width:213px">NEWSLETTER</div>
  <div class="abs col-list" style="left:651px">Register your email address to get more<br>information about us and our services</div>
  <div class="abs news-input">Email Address</div>
  <div class="abs news-btn">SUBSCRIBE</div>
</footer>
<div class="abs copyright">COPYRIGHT © 2019 456ABRI.FR. ALL RIGHTS RESERVED.</div>

</body>
</html>
```